Microsite for a private healthcare provider

The design I need (PSD file) is for a company offering two services:
1. Recruitment of nurses
2. Provider a private health care: prenatal classes, vaccines for travellers
Here's a website we designed and we would like a similar style in terms of layout. Please note there will be about the same amount of content (text) http://lumeravisuel.example/fr
Main menu with 4 sections:
Accueil |Agence de placement | Soins privés | Contact
Links to their social media accounts:
https://twitter.com/Valdoriel
https://www.facebook.com/pages/Valdoriel-Agence-de-placement-en-soins-de-sant%C3%A9/482039571620413
Contact details:
TÉL. (555) 302-4419
TÉLEC. (555) 302-9154
1187 boulevard Ormelande, suite 3400
St-Hubert (Québec), K8W 5M3
Target Market(s)
Nurses looking for a job, Expecting women, People about to travel and seeking vaccines
Industry/Entity Type
Healthcare
Requirements
Must have
- 1- Must be responsive for mobiles and tablets
2 - Twitter feed
3 - Google maps at the end next to their contact details
4- Two contact forms:
Form for people to send in their resume.
The form title is: Postulez
Fields required:
Nom complet
Courriel
Téléphone
Années d'expérience (with drop down list: 1-2 ans, 3-5 ans, 5 ans et plus)
Choose file (possibility to attach a cv)
Message
Form for requesting information
Form title is: Demande d'informations
Fields are:
Nom complet
Téléphone
Courriel
Message
Nice to have
- Here are some images on Pixvane Images the client likes, you can use for inspiration.
Agence de placement section:
File #40581936
File #6417283
File #8250946
File #5092734
File #47306152
File #39847201
File #26415037
Soins privés section:
File #33782519
File #31940285
File #34617092
File #48053276
File #27360458
File #29518064
File #42870315
File #6783052
File #35104827

```html
<!DOCTYPE html>
<html lang="fr">
<head>
<meta charset="utf-8">
<title>Valdoriel – Soins privés</title>
<link rel="stylesheet" href="https://fonts.googleapis.com/css2?family=Open+Sans:ital,wght@0,400;0,600;0,700;1,400&display=swap">
<style>
  :root {
    --green: #8fae1b;
    --blue: #1d4f9a;
    --navy: #1b4a92;
    --ink: #3d3d3d;
    --muted: #8a8a8a;
    --line: #e6e6e6;
    --cream: #f7f8ee;
    --band: #3b3b3b;
    --field: #ffffff;
    --field-line: #e2e4d8;
    --btn-grey: #8c8c8c;
  }
  * { box-sizing: border-box; margin: 0; padding: 0; }
  html, body { width: 784px; height: 1200px; overflow: hidden; }
  body {
    position: relative;
    background: #ffffff;
    font-family: "Open Sans", Arial, sans-serif;
    color: var(--ink);
  }

  /* Header */
  .site-header {
    position: absolute; left: 0; top: 0; width: 784px; height: 43px;
    background: #fff; border-top: 2px solid var(--green);
    border-bottom: 1px solid #e4e4e4; z-index: 3;
  }
  .brand {
    position: absolute; left: 123px; top: 8px;
    display: flex; align-items: center; gap: 6px;
    font-weight: 700; font-size: 21px; color: var(--blue); letter-spacing: -0.3px;
  }
  .brand-dot { width: 10px; height: 10px; background: var(--green); }
  .main-nav { position: absolute; top: 12px; left: 380px; display: flex; }
  .main-nav a {
    font-size: 10px; font-weight: 600; color: #6b6b6b; text-decoration: none;
    padding: 3px 8px; height: 19px; line-height: 13px; margin-right: 4px;
  }
  .main-nav a.is-active { background: var(--green); color: #fff; border-radius: 2px; }

  /* Hero band */
  .hero-photo {
    position: absolute; left: 0; top: 43px; width: 784px; height: 266px;
    background: linear-gradient(90deg, #dbe3ea 0%, #eef1f3 30%, #f3f3f1 60%, #dfe6ec 100%);
  }

  /* Main card */
  .content-card {
    position: absolute; left: 120px; top: 93px; width: 546px; height: 738px;
    background: #fff; box-shadow: 0 0 6px rgba(0,0,0,0.12); z-index: 2;
  }
  .services { position: absolute; left: 0; top: 0; width: 383px; height: 100%; }
  .services-title {
    position: absolute; left: 16px; top: 12px;
    font-size: 19px; font-weight: 400; color: var(--blue); line-height: 24px;
  }
  .services-intro {
    position: absolute; left: 17px; top: 40px; width: 340px;
    font-size: 8.8px; line-height: 12px; color: #555;
  }
  .service-list { list-style: none; position: absolute; left: 18px; top: 81px; width: 350px; }
  .service { position: relative; height: 108px; }
  .service::after {
    content: ""; position: absolute; left: 0; right: 0; top: 95px;
    border-top: 1px solid var(--line);
  }
  .service:last-child::after { display: none; }
  .service-photo { position: absolute; left: 0; top: 0; width: 101px; height: 82px; }
  .service-body { position: absolute; left: 112px; top: -2px; width: 238px; }
  .service-title {
    font-size: 11.5px; font-weight: 400; color: #333; line-height: 15px;
    white-space: nowrap;
  }
  .service-desc {
    font-size: 6.8px; line-height: 11px; color: var(--muted); margin-top: 3px;
    width: 236px; height: 44px; overflow: hidden;
  }
  .service-actions { display: flex; align-items: center; gap: 9px; margin-top: 5px; }
  .btn-book {
    width: 96px; height: 17px; font-size: 7.5px; line-height: 17px; text-align: center;
    background: var(--btn-grey); color: #fff; text-transform: uppercase;
  }
  .btn-book.is-active { background: var(--green); }
  .price { font-size: 8px; color: #555; }
  .price strong { font-size: 10.5px; color: var(--green); font-weight: 600; }

  /* Sidebar */
  .sidebar {
    position: absolute; left: 383px; top: 0; width: 163px; height: 100%;
    background: var(--cream); border-left: 1px solid #eceee2;
  }
  .sidebar-note { position: absolute; left: 15px; top: 15px; width: 135px; font-size: 8px; line-height: 11px; color: #444; }
  .btn-apply-now {
    position: absolute; left: 15px; top: 56px; width: 132px; height: 29px;
    background: var(--navy); color: #fff; font-size: 9.5px; font-weight: 600;
    text-align: center; line-height: 27px; border: 1px solid #143a72;
  }
  .sidebar-heading { position: absolute; left: 15px; font-size: 15px; color: var(--green); font-weight: 400; }
  .apply-form { position: absolute; left: 15px; top: 134px; width: 132px; }
  .field {
    height: 18px; margin-bottom: 3px; background: var(--field); border: 1px solid var(--field-line);
    font-size: 6.5px; color: #999; padding: 4px 7px; position: relative;
  }
  .field-select .caret {
    position: absolute; right: 0; top: 0; width: 18px; height: 16px; background: #3a3a3a;
  }
  .field-file .browse {
    position: absolute; right: -1px; top: -1px; width: 46px; height: 18px; background: #3a3a3a;
    color: #fff; font-size: 6.5px; text-align: center; line-height: 18px;
  }
  .field-message { height: 47px; }
  .btn-apply {
    width: 68px; height: 18px; margin-top: 8px; background: var(--green); color: #fff;
    font-size: 9px; text-align: center; line-height: 18px;
  }
  .sidebar-rule { position: absolute; left: 0; top: 338px; width: 162px; border-top: 1px solid #e8eadc; }
  .testimonial {
    position: absolute; left: 15px; top: 389px; width: 134px;
    font-size: 9.5px; line-height: 12.6px; font-style: italic; color: #555;
  }
  .author { position: absolute; left: 15px; top: 565px; display: flex; align-items: center; gap: 7px; }
  .author-photo { width: 30px; height: 30px; border-radius: 50%; background: linear-gradient(135deg, #c9a385, #8a6248); }
  .author-name { font-size: 10px; color: var(--blue); font-style: italic; }
  .author-role { font-size: 6.5px; color: #666; }

  /* Info band */
  .info-band {
    position: absolute; left: 0; top: 859px; width: 784px; height: 95px; background: var(--band);
  }
  .info-tab {
    position: absolute; left: 120px; top: 0; width: 56px; height: 95px; background: var(--green);
  }
  .info-tab span {
    position: absolute; left: 28px; top: 47px; width: 95px;
    transform: translate(-50%, -50%) rotate(-90deg);
    color: #fff; font-size: 11px; line-height: 13px; text-align: center;
  }
  .info-form .field { position: absolute; width: 109px; height: 15px; padding: 2px 6px; border: 0; margin: 0; }
  .info-form .field-message { width: 106px; height: 34px; }
  .btn-send {
    position: absolute; left: 306px; top: 57px; width: 106px; height: 17px;
    background: var(--green); color: #fff; font-size: 10px; text-align: center; line-height: 17px;
  }
  .contact-details { position: absolute; left: 489px; top: 12px; color: #d6d6d6; }
  .contact-details h2 { font-size: 14px; font-weight: 400; color: #fff; margin-bottom: 4px; }
  .contact-line { display: flex; gap: 5px; font-size: 8.5px; line-height: 11px; }
  .contact-line svg { flex: none; margin-top: 2px; }

  /* Map */
  .map {
    position: absolute; left: 0; top: 954px; width: 784px; height: 206px;
    background: linear-gradient(160deg, #ecebe4 0%, #e6e5dd 60%, #dfe6cf 100%);
  }

  /* Footer */
  .site-footer { position: absolute; left: 120px; top: 1168px; display: flex; gap: 10px; }
  .site-footer a { font-size: 7px; color: #999; text-decoration: none; }
</style>
</head>
<body>

<header class="site-header">
  <div class="brand"><span class="brand-dot"></span>Valdoriel</div>
  <nav class="main-nav">
    <a href="#">Accueil</a>
    <a href="#">Agence de placement</a>
    <a href="#" class="is-active">Soins privés</a>
    <a href="#">Contact</a>
  </nav>
</header>

<div class="hero-photo" role="img" aria-label="Photo floue de personnel soignant souriant"></div>

<main class="content-card">
  <section class="services">
    <h1 class="services-title">Soins au privé</h1>
    <p class="services-intro">Lorem Ipsum is simply dummy text of the printing and typesetting industry. Lorem Ipsum has been the industry's standard dummy text everspecimen book.</p>
    <ul class="service-list">
      <li class="service">
        <div class="service-photo" role="img" aria-label="Médecin examinant une femme enceinte" style="background:linear-gradient(135deg,#e9e4df,#c9a88e)"></div>
        <div class="service-body">
          <h3 class="service-title">Enhanced Maternity Package</h3>
          <p class="service-desc">If you are thinking of having a baby, our Enhanced Maternity package is for you. While your core plan will cover you for 3 night's private accommodation in a public hospital, by adding this package, you get access to a range of enhanced maternity benefits</p>
          <div class="service-actions"><span class="btn-book">Prenez rendez-vous</span><span class="price">Price : <strong>$150.00</strong></span></div>
        </div>
      </li>
      <li class="service">
        <div class="service-photo" role="img" aria-label="Bébé recevant un vaccin" style="background:linear-gradient(135deg,#8aa7c4,#e2c3ad)"></div>
        <div class="service-body">
          <h3 class="service-title">Meningococcal (MPSV4)</h3>
          <p class="service-desc">If you are thinking of having a baby, our Enhanced Maternity package is for you. While your core plan will cover you for 3 night's private accommodation in a public hospital, by adding this package, you get access to a range of enhanced maternity benefits</p>
          <div class="service-actions"><span class="btn-book is-active">Prenez rendez-vous</span><span class="price">Price : <strong>$150.00</strong></span></div>
        </div>
      </li>
      <li class="service">
        <div class="service-photo" role="img" aria-label="Femme enceinte allongée lors d'un examen" style="background:linear-gradient(135deg,#e8e1dc,#d6a2a8)"></div>
        <div class="service-body">
          <h3 class="service-title">Shingles (Herpes Zoster) (10/06/09)</h3>
          <p class="service-desc">If you are thinking of having a baby, our Enhanced Maternity package is for you. While your core plan will cover you for 3 night's private accommodation in a public hospital, by adding this package, you get access to a range of enhanced maternity benefits</p>
          <div class="service-actions"><span class="btn-book">Prenez rendez-vous</span><span class="price">Price : <strong>$150.00</strong></span></div>
        </div>
      </li>
      <li class="service">
        <div class="service-photo" role="img" aria-label="Seringue de vaccin près d'un bras" style="background:linear-gradient(135deg,#c8d6e4,#d6a98b)"></div>
        <div class="service-body">
          <h3 class="service-title">Tdap (Tetanus, Diphtheria, Pertussis) (5/9/13)</h3>
          <p class="service-desc">If you are thinking of having a baby, our Enhanced Maternity package is for you. While your core plan will cover you for 3 night's private accommodation in a public hospital, by adding this package, you get access to a range of enhanced maternity benefits</p>
          <div class="service-actions"><span class="btn-book">Prenez rendez-vous</span><span class="price">Price : <strong>$150.00</strong></span></div>
        </div>
      </li>
      <li class="service">
        <div class="service-photo" role="img" aria-label="Bébé souriant pendant une vaccination" style="background:linear-gradient(135deg,#7fb7a6,#e0b59a)"></div>
        <div class="service-body">
          <h3 class="service-title">Pneumococcal Polysaccharide VIS</h3>
          <p class="service-desc">If you are thinking of having a baby, our Enhanced Maternity package is for you. While your core plan will cover you for 3 night's private accommodation in a public hospital, by adding this package, you get access to a range of enhanced maternity benefits</p>
          <div class="service-actions"><span class="btn-book">Prenez rendez-vous</span><span class="price">Price : <strong>$150.00</strong></span></div>
        </div>
      </li>
      <li class="service">
        <div class="service-photo" role="img" aria-label="Mains sur un ventre de femme enceinte" style="background:linear-gradient(135deg,#e6c2a2,#b9835e)"></div>
        <div class="service-body">
          <h3 class="service-title">Enhanced Maternity Package</h3>
          <p class="service-desc">If you are thinking of having a baby, our Enhanced Maternity package is for you. While your core plan will cover you for 3 night's private accommodation in a public hospital, by adding this package, you get access to a range of enhanced maternity benefits</p>
          <div class="service-actions"><span class="btn-book">Prenez rendez-vous</span><span class="price">Price : <strong>$150.00</strong></span></div>
        </div>
      </li>
    </ul>
  </section>

  <aside class="sidebar">
    <p class="sidebar-note">Nous acceptons actuellement les candidatures via notre formulaire en ligne seulement.</p>
    <div class="btn-apply-now">POSTULEZ MAINTENANT</div>
    <h2 class="sidebar-heading" style="top:99px">Postulez</h2>
    <form class="apply-form">
      <div class="field">Nom complet</div>
      <div class="field">Courriel</div>
      <div class="field">Téléphone</div>
      <div class="field field-select">Années d'expérience
        <span class="caret"><svg width="18" height="16" viewBox="0 0 18 16"><path d="M6 7h6l-3 3z" fill="#fff"/></svg></span>
      </div>
      <div class="field field-file">Choisir le fichier<span class="browse">BROWSE</span></div>
      <div class="field field-message">Un message</div>
      <div class="btn-apply">APPLY</div>
    </form>
    <div class="sidebar-rule"></div>
    <h2 class="sidebar-heading" style="top:358px">Success Stories</h2>
    <blockquote class="testimonial">“I have had so many wonderful experiences in Australia and have had great feedback about my work,” says LINA MARCHETTI who was born in Terala. “There are quite a few Indians here and I don't even miss my home. After one year of work with Corvenna, I am going to apply for a Master in Psychiatry. I am grateful to Pierre and Sofia for always being there for me when I need them.”</blockquote>
    <div class="author">
      <div class="author-photo" role="img" aria-label="Portrait de l'auteure du témoignage"></div>
      <div>
        <div class="author-name">Lina Marchetti</div>
        <div class="author-role">Acting care Manager</div>
      </div>
    </div>
  </aside>
</main>

<section class="info-band">
  <div class="info-tab"><span>Demande d'informations</span></div>
  <form class="info-form">
    <div class="field" style="left:189px;top:21px">Nom complet</div>
    <div class="field" style="left:189px;top:39px">Téléphone</div>
    <div class="field" style="left:189px;top:57px">Courriel</div>
    <div class="field field-message" style="left:306px;top:21px">Un message</div>
    <div class="btn-send">SEND</div>
  </form>
  <div class="contact-details">
    <h2>Contact Details</h2>
    <div class="contact-line">
      <svg width="8" height="10" viewBox="0 0 8 10"><path d="M4 0a3.5 3.5 0 0 0-3.5 3.5C.5 6 4 10 4 10s3.5-4 3.5-6.5A3.5 3.5 0 0 0 4 0zm0 5a1.4 1.4 0 1 1 0-2.8A1.4 1.4 0 0 1 4 5z" fill="#d6d6d6"/></svg>
      <span>1187 boulevard Ormelande, suite 3400<br>St-Hubert (Québec), K8W 5M3</span>
    </div>
    <div class="contact-line" style="margin-top:7px">
      <svg width="9" height="9" viewBox="0 0 10 10"><path d="M2 0l2 2.5-1.2 1.3a6 6 0 0 0 3.4 3.4L7.5 6 10 8l-1.2 1.6C5 10 0 5 .4 1.2z" fill="#d6d6d6"/></svg>
      <span>(555) 302-4419</span>
    </div>
    <div class="contact-line">
      <svg width="9" height="9" viewBox="0 0 10 10"><rect x="0" y="3" width="10" height="6" rx="1" fill="#d6d6d6"/><rect x="2" y="0" width="6" height="4" fill="#d6d6d6"/></svg>
      <span>(555) 302-9154</span>
    </div>
  </div>
</section>

<div class="map" role="img" aria-label="Carte de localisation du bureau à St-Hubert"></div>

<footer class="site-footer">
  <a href="#">Accueil</a>
  <a href="#">Agence de placement</a>
  <a href="#">Soins privés</a>
  <a href="#">Contact</a>
</footer>

</body>
</html>
```